Business Card for Flight Instructor/Commercial Pilot

I need a business card for myself as a Flight Instructor. I'm a certificated flight instructor at a local flight school in St Paul, MN and want to have a business card that I can give out both to prospective students and also to prospective employers in commercial/business aviation. The business card should have a few elements to it (my name, my position, and my ZRT certifications:
Dorian Welkes, MBA
Flight Instructor
CFI, CFII, AGI, IGI
Then lastly, I'd like it to include my phone number for calls or texts, my email address, and my Corvanet url. I'll provide all of these at a later point.

If we can include some kind of aviation graphic, that's great, but I don't currently have a logo and I don't necessarily need one, so don't feel like a logo is required here, it's not. I'm but I'm open to whatever you might put together. But I honestly don't need a logo, just good design with a simple graphic element to draw a little interest.
I'd also like to add a short tag line. A few ideas I have are:
- Fly Smart. Stay Humble. Never Stop Learning.
- Train smart. Fly safe. Have fun.
- Master the craft. Enjoy the flight.

For the back side, I'm open to ideas on what to put there. maybe the tagline could go there, or a QR code for my Corvanet page, or maybe something else.

Target audience is both prospective students who are interested in learning to fly (or adding more ratings) and commercial aviation companies that could be potential employer for me in commercial aviation. Trying to portray a sense of professionalism, trust, and high level of competency.

The business card doesn’t have to be standard (rectangular with square corners) and I’m open to suggestions for based on the design.
Lastly, I just don't want the design created by AI.
Let me know if you need any further info. Thanks!

```html
<!DOCTYPE html>
<html lang="en">
<head>
<meta charset="utf-8">
<title>Dorian Welkes, MBA – Flight Instructor Business Card</title>
<link rel="stylesheet" href="https://fonts.googleapis.com/css2?family=Montserrat:wght@400;500;600;700&display=swap">
<style>
  :root {
    --navy: #1b2740;
    --navy-deep: #141d31;
    --gold: #a8834a;
    --gold-light: #c9a56a;
    --ivory: #efede8;
    --ink: #1e2a44;
    --text-grey: #3a3f4a;
    --stage: #e4e4e6;
  }
  * { box-sizing: border-box; margin: 0; padding: 0; }
  html, body {
    width: 1200px; height: 800px; overflow: hidden;
    background: var(--stage);
    font-family: "Montserrat", Arial, sans-serif;
  }
  .sheet {
    width: 1200px; height: 800px;
    display: flex; align-items: center; justify-content: center; gap: 32px;
  }
  .card {
    position: relative;
    width: 560px; height: 320px;
    border-radius: 22px;
    overflow: hidden;
    box-shadow: 0 6px 18px rgba(0,0,0,.18);
  }

  /* Back side */
  .card-back { background: var(--navy); }
  .back-plane {
    position: absolute; left: 230px; top: 48px;
    width: 100px; height: 26px;
  }
  .tagline {
    position: absolute; left: 0; right: 0; top: 96px;
    text-align: center;
    color: #dcdfe6;
    font-weight: 500; font-size: 15px; letter-spacing: 5px; line-height: 26px;
    text-transform: uppercase;
  }
  .tag-rule {
    position: absolute; top: 168px; height: 1px; width: 130px;
    background: var(--gold);
  }
  .tag-rule.left { left: 136px; }
  .tag-rule.right { right: 136px; }
  .tag-mark {
    position: absolute; left: 272px; top: 160px;
    width: 16px; height: 16px; border-radius: 50%;
    background: var(--gold-light);
  }
  .back-ridge {
    position: absolute; left: 0; right: 0; bottom: 0; height: 120px;
  }

  /* Front side */
  .card-front { background: var(--ivory); }
  .front-photo {
    position: absolute; right: 0; top: 0;
    width: 290px; height: 290px;
    background: linear-gradient(200deg, #f2f2f2 0%, #bdbdbd 45%, #8c8c8c 100%);
    -webkit-mask-image: linear-gradient(90deg, transparent 0%, #000 30%);
            mask-image: linear-gradient(90deg, transparent 0%, #000 30%);
  }
  .front-band { position: absolute; left: 0; bottom: 0; width: 560px; height: 60px; }
  .accent-rule {
    position: absolute; left: 34px; top: 96px; width: 1.5px; height: 172px;
    background: var(--gold);
  }
  .identity { position: absolute; left: 52px; top: 68px; }
  .name {
    color: var(--ink); font-weight: 700; font-size: 23px; letter-spacing: 1.6px;
    text-transform: uppercase;
  }
  .role {
    margin-top: 6px;
    color: var(--gold); font-weight: 600; font-size: 14px; letter-spacing: 3px;
    text-transform: uppercase;
  }
  .certs {
    margin-top: 10px;
    color: var(--ink); font-weight: 600; font-size: 14px; letter-spacing: 1.4px;
  }
  .divider { margin-top: 12px; width: 190px; height: 1px; background: var(--gold); }
  .contact-list { list-style: none; margin-top: 14px; }
  .contact-item {
    display: flex; align-items: center; gap: 12px;
    color: var(--text-grey); font-size: 12.5px; font-weight: 500;
    height: 25px;
  }
  .contact-icon {
    width: 18px; height: 18px; border-radius: 50%;
    background: var(--gold);
    display: flex; align-items: center; justify-content: center;
    flex: none;
  }
  .contact-icon svg { width: 10px; height: 10px; }
</style>
</head>
<body>
<main class="sheet">

  <section class="card card-back" aria-label="Card back">
    <div class="back-plane" role="img" aria-label="Small gold aircraft emblem, front view"
         style="background: radial-gradient(ellipse at center, var(--gold-light) 0%, rgba(168,131,74,.35) 55%, transparent 75%);"></div>
    <p class="tagline">Master the craft.<br>Enjoy the flight.</p>
    <span class="tag-rule left"></span>
    <span class="tag-mark" role="img" aria-label="Gold compass star"></span>
    <span class="tag-rule right"></span>
    <div class="back-ridge" role="img" aria-label="Embossed mountain range silhouette"
         style="background: linear-gradient(180deg, rgba(20,29,49,0) 0%, rgba(20,29,49,.55) 55%, var(--navy-deep) 100%);"></div>
  </section>

  <section class="card card-front" aria-label="Card front">
    <div class="front-photo" role="img" aria-label="Black and white photo of an airliner wing above the clouds"></div>

    <svg class="front-band" viewBox="0 0 560 60" preserveAspectRatio="none" aria-hidden="true">
      <path d="M0 36 H300 L312 28 H560 V60 H0 Z" fill="var(--navy)"/>
      <path d="M0 34 H299 L311 26 H560" fill="none" stroke="var(--gold)" stroke-width="1.2"/>
    </svg>

    <span class="accent-rule"></span>

    <div class="identity">
      <h1 class="name">Dorian Welkes, MBA</h1>
      <p class="role">Flight Instructor</p>
      <p class="certs">CFI, CFII, AGI, IGI</p>
      <div class="divider"></div>
      <ul class="contact-list">
        <li class="contact-item">
          <span class="contact-icon">
            <svg viewBox="0 0 10 10"><path d="M2 1 L3.6 1 L4.2 3 L3.2 3.8 Q4 5.6 6.2 6.8 L7 5.8 L9 6.4 L9 8 Q8.6 9 7.5 9 Q2.5 8 1 2.5 Q1 1.2 2 1 Z" fill="#fff"/></svg>
          </span>
          651.555.0148
        </li>
        <li class="contact-item">
          <span class="contact-icon">
            <svg viewBox="0 0 10 10"><rect x="1" y="2.2" width="8" height="5.6" fill="none" stroke="#fff" stroke-width="1"/><path d="M1 2.4 L5 5.4 L9 2.4" fill="none" stroke="#fff" stroke-width="1"/></svg>
          </span>
          dorian.welkes@loftwardflight.com
        </li>
        <li class="contact-item">
          <span class="contact-icon"></span>
          corvanet.com/in/dorianwelkes
        </li>
      </ul>
    </div>
  </section>

</main>
</body>
</html>
```